Eye catching Bottle label for pink gin targeting women 25+

We need a new label for a re-launch of our shimmering strawberry pink Gin Cordial. We would like it to look premium and eye catching on the shelf. We have 2 labels we require, one for 200ml bottle (2x2 inches) and one for 500ml bottle 4x4 inches). Label must state the ml of the bottle abd that it is 18.75%Vol. Also say Shimmering Strawberry Gin Cordial with the brand name at the top - Harlow Vale Distillers. We have a logo but it doesn't need to be used if it doesn't work with the design/colours. The gin is presented in a clear bottle and is pink and sparkly. See uploaded image for reference.

Target Market(s)

Women aged 25-45

Font styles to use
Decorative

Colors
f59296
fbd4d5
eea4c8

Requirements
Must have
• Bottle size - 500ml/200ml
• Must say 18.75% Vol
• Must have brand name - Harlow Vale Distillers
• Must have product name - Glistening Rose Raspberry
• Must say - Gin Cordial
Nice to have
• Some sort of floral or swirley background detail would be nice
Should not have
• Must not appeal to children

```html
<!DOCTYPE html>
<html lang="en">
<head>
<meta charset="utf-8">
<title>Harlow Vale Distillers – Glistening Rose Raspberry Gin Cordial Label</title>
<link rel="stylesheet" href="https://fonts.googleapis.com/css2?family=Cinzel:wght@400&family=Tinos&display=swap">
<style>
  :root {
    --coral: #f59296;
    --blush: #fbd4d5;
    --blush-line: #f7b9bc;
    --pattern-pink: #fbe3e5;
    --paper: #ffffff;
    --mauve: #9c6375;
    --mauve-deep: #8a5366;
    --brand-grey: #4a4548;
    --ink: #111111;
  }
  * { margin: 0; padding: 0; box-sizing: border-box; }
  html, body {
    width: 1200px;
    height: 1200px;
    overflow: hidden;
    background: var(--paper);
  }
  .label {
    position: relative;
    width: 1200px;
    height: 1200px;
    overflow: hidden;
    background: var(--paper);
  }
  .berry-pattern {
    position: absolute;
    inset: 0;
    background:
      radial-gradient(circle at 50% 50%, rgba(255,255,255,0.55) 0%, rgba(255,255,255,0) 60%),
      linear-gradient(180deg, var(--pattern-pink) 0%, #fcebec 50%, var(--pattern-pink) 100%);
  }
  .brand-name {
    position: absolute;
    top: 120px;
    left: 0;
    width: 100%;
    text-align: center;
    font-family: "Cinzel", serif;
    font-weight: 400;
    font-size: 70px;
    line-height: 1.15;
    color: var(--brand-grey);
  }
  .brand-mark {
    display: block;
    width: 26px;
    height: 26px;
    margin: 0 auto 18px;
    border-radius: 50%;
    background: var(--brand-grey);
  }
  .product-title {
    position: absolute;
    top: 540px;
    left: 0;
    width: 1200px;
    height: 320px;
  }
  .product-title text {
    font-family: "Cinzel", serif;
    font-weight: 400;
    paint-order: stroke;
    stroke: rgba(255,255,255,0.85);
    stroke-width: 10px;
    stroke-linejoin: round;
  }
  .product-title .line-one { fill: var(--mauve); }
  .product-title .line-two { fill: var(--mauve-deep); }
  .rule {
    position: absolute;
    left: 0;
    width: 100%;
    height: 7px;
    background: var(--blush-line);
  }
  .rule--top { top: 874px; }
  .rule--bottom { top: 997px; }
  .category-band {
    position: absolute;
    top: 904px;
    left: 0;
    width: 100%;
    height: 78px;
    background: var(--coral);
    display: flex;
    align-items: center;
    justify-content: center;
    font-family: "Tinos", serif;
    font-size: 58px;
    color: var(--paper);
  }
  .bottle-details {
    position: absolute;
    top: 1100px;
    left: 110px;
    right: 118px;
    display: flex;
    justify-content: space-between;
    font-family: "Tinos", serif;
    font-size: 40px;
    color: var(--ink);
  }
</style>
</head>
<body>
  <main class="label">
    <div class="berry-pattern" role="img" aria-label="Repeating pattern of pale pink berry silhouettes covering the label background"></div>

    <header class="brand-name">
      <span class="brand-mark"></span>
      Harlow Vale<br>Distillers
    </header>

    <svg class="product-title" viewBox="0 0 1200 320" aria-label="Glistening Rose Raspberry">
      <text class="line-one" x="600" y="120" text-anchor="middle" font-size="108" textLength="960" lengthAdjust="spacingAndGlyphs">GLISTENING ROSE</text>
      <text class="line-two" x="600" y="280" text-anchor="middle" font-size="176" textLength="950" lengthAdjust="spacingAndGlyphs">RASPBERRY</text>
    </svg>

    <div class="rule rule--top"></div>
    <div class="category-band">Gin Cordial</div>
    <div class="rule rule--bottom"></div>

    <footer class="bottle-details">
      <span class="abv">18.75% Vol</span>
      <span class="volume">500ml</span>
    </footer>
  </main>
</body>
</html>
```